Wellbeing Challenge Posters

We are running a wellbeing challenge. Every week we run a challenge under a different theme. We need 5 themes to start with:
- Connect
- Be mindful
- Get moving
- Give
- Grow your mind

Each theme needs to have the following:
1. Match the colours of the icons provided under each
2. Have a clear place for the word where these can be changed but utilising the same theme. For example, under connect, we will run a number of different challenges but the theme will remain the same.
3. Each theme will have the following:
-This week's challenge
- Points
4. Brightwell Weekly logo

The content under each of the themes will be as follows:

1. Connect
This week's challenge: Have a shared meal with your team - take a photo and post it on the challenge forum
Points: 10 points per person that attended if you had more than 75% of your team

2. Be Mindful
This week's challenge: START something that will improve your wellbeing, STOP something that is bad for you - Be mindful of how you feel at the end of the week.

3. Get moving:
This week's challenge: Do a minimum 150 minutes of exercise this week required for good general health - try something new!
Points: Take your usual 1 point per 30 mins exercise but give yourself an additional 10 points if you do 150mins or more for the week.

4. Give:
This week's challenge: Do a random act of kindness every day this week
Points: 1 point per day PLUS 10 points if you complete 1 every day

5. Grow Your Mind
This week's challenge: Learn something new every day! Read a research paper, watch a ZIVO talk, DIY, learn something about your workmates

```html
<!DOCTYPE html>
<html lang="en">
<head>
<meta charset="utf-8">
<title>Brightwell Weekly – Connect</title>
<link rel="stylesheet" href="https://fonts.googleapis.com/css2?family=Questrial&display=swap">
<style>
  :root {
    --teal: #45a2a2;
    --teal-light: #5bb2b0;
    --ink: #1f1f1f;
    --grey: #6b6b6b;
    --paper: #ffffff;
    --photo-top: #f4f1ee;
    --photo-mid: #eef0ea;
    --photo-low: #f3ebe4;
  }
  * { margin: 0; padding: 0; box-sizing: border-box; }
  html, body {
    width: 1200px; height: 1000px; overflow: hidden;
    background: var(--paper);
    font-family: "Questrial", "Century Gothic", sans-serif;
  }
  .canvas { position: relative; width: 1200px; height: 1000px; }
  .poster { position: absolute; left: 228px; top: 5px; width: 697px; height: 988px; }
  .poster-frame { position: absolute; inset: 0; }
  .block { position: absolute; left: 380px; width: 530px; text-align: center; }
  .brand {
    position: absolute; left: 455px; top: 90px;
    display: flex; align-items: center; gap: 16px;
    color: var(--grey); font-size: 40px; line-height: 1.05;
  }
  .brand-dot { width: 26px; height: 26px; border-radius: 50%; background: var(--teal); flex: none; }
  .heading { color: var(--teal); font-size: 36px; line-height: 1; }
  .body-copy { color: var(--ink); font-size: 22px; line-height: 33px; margin-top: 14px; }
  .challenge { top: 280px; }
  .points { top: 550px; }
  .contact { top: 840px; color: var(--ink); }
  .contact-title { font-size: 23px; letter-spacing: 0.3px; }
  .contact-line {
    display: flex; align-items: center; justify-content: center; gap: 6px;
    font-size: 19px; margin-top: 10px;
  }
  .contact-line svg { flex: none; }
  .theme-badge {
    position: absolute; left: 313px; top: 400px; width: 184px; height: 184px;
    border-radius: 50%; background: var(--paper); border: 3px solid var(--teal);
  }
  .theme-name {
    position: absolute; top: 28px; width: 100%; text-align: center;
    color: var(--teal); font-size: 15px; font-weight: bold; letter-spacing: 2px;
  }
  .theme-icon {
    position: absolute; left: 42px; top: 52px; width: 94px; height: 94px;
    border-radius: 50%; background: var(--teal);
  }
  .theme-tagline {
    position: absolute; top: 152px; width: 100%; text-align: center;
    color: var(--ink); font-size: 11px; font-weight: bold;
  }
</style>
</head>
<body>
<div class="canvas">
  <svg class="poster-frame" style="left:228px;top:5px;width:697px;height:988px;position:absolute" viewBox="228 5 697 988" aria-hidden="true">
    <defs>
      <linearGradient id="photo-wash" x1="0" y1="0" x2="0" y2="1">
        <stop offset="0" stop-color="var(--photo-top)"/>
        <stop offset="0.5" stop-color="var(--photo-mid)"/>
        <stop offset="1" stop-color="var(--photo-low)"/>
      </linearGradient>
    </defs>
    <rect x="228" y="5" width="697" height="988" fill="var(--teal)"/>
    <path d="M300,18 L910,18 L910,978 L300,978 C320,860 360,770 425,700 C478,640 478,420 420,385 C345,335 305,210 300,18 Z" fill="var(--paper)"/>
    <rect x="914" y="11" width="5" height="975" fill="none" stroke="var(--paper)" stroke-width="1.5"/>
  </svg>
  <svg role="img" aria-label="Soft faded photo of colleagues sharing a meal with salad, fruit bowl and cups of tea" style="position:absolute;left:228px;top:5px;width:697px;height:988px" viewBox="228 5 697 988">
    <path d="M300,18 L910,18 L910,978 L300,978 C320,860 360,770 425,700 C478,640 478,420 420,385 C345,335 305,210 300,18 Z" fill="url(#photo-wash)" opacity="0.55"/>
  </svg>

  <div class="brand">
    <span>Brightwell<br>Weekly</span>
    <span class="brand-dot"></span>
  </div>

  <section class="block challenge">
    <h2 class="heading">The week’s challenge</h2>
    <p class="body-copy">Have a shared meal with your team - take<br>a photo and post it on the challenge<br>forum</p>
  </section>

  <div class="theme-badge">
    <div class="theme-name">CONNECT</div>
    <div class="theme-icon" role="img" aria-label="Connect theme icon of three people linked together"></div>
    <div class="theme-tagline">Engage with others</div>
  </div>

  <section class="block points">
    <h2 class="heading">Point</h2>
    <p class="body-copy">10 points per person that attended if<br>you had more than 75% of your team</p>
  </section>

  <section class="block contact">
    <div class="contact-title">CONTACT US NOW</div>
    <div class="contact-line">
      <svg width="16" height="18" viewBox="0 0 16 18"><path d="M4 1 L7 5 L5 7 C6 10 8 12 10 13 L12 11 L15 14 L13 17 C7 16 2 10 1 4 Z" fill="none" stroke="var(--ink)" stroke-width="1.2"/></svg>
      <span>04 215 8830</span>
    </div>
    <div class="contact-line">
      <svg width="24" height="16" viewBox="0 0 24 16"><rect x="1" y="1" width="22" height="14" fill="none" stroke="var(--ink)" stroke-width="1.3"/><path d="M1 1 L12 9 L23 1" fill="none" stroke="var(--ink)" stroke-width="1.3"/></svg>
      <span>hello@brightwellteams.co.nz</span>
    </div>
  </section>
</div>
</body>
</html>
```